Managed IT services business card design

We haven't needed a business card since the founding of the business in 2005. All our clients have been coming through word of mouth. And lately more and more existing clients are requesting for our business cards to pass on to their contacts in recommending us.
So we needing a business card design. We use various innovative solutions and methodologies to provide IT services to small businesses in managing their IT systems. Our role is the same as an in-house, full-time IT Manager for our clients, but outsourced. So we take care of all our clients' IT needs, just as an IT Manager would be expected to perform.
We have a holding website, which we're happy to leave for now. If we can use the same logo would be great - www.tegvu.com.au
Preferred colours are shades of are white, grey and black.
We pride our business with the following traits: proactive, good service, prompt response, trustworthy.
Target Market(s)
Small businesses of any industry
Industry/Entity Type
Business

```html
<!DOCTYPE html>
<html lang="en">
<head>
<meta charset="utf-8">
<title>tegvu business card</title>
<link href="https://fonts.googleapis.com/css2?family=Arimo:wght@400&display=swap" rel="stylesheet">
<style>
  :root {
    --backdrop: #d6d6d6;
    --paper: #ffffff;
    --ink: #1f1f1f;
    --ink-soft: #555555;
    --dark-card: #2a2422;
    --band-grey: #5d6165;
    --rule: #3a3a3a;
  }
  * { margin: 0; padding: 0; box-sizing: border-box; }
  html, body {
    width: 1200px; height: 680px; overflow: hidden;
    background: var(--backdrop);
    font-family: "Arimo", Arial, sans-serif;
  }
  .canvas {
    position: relative; width: 1200px; height: 680px;
    display: flex; align-items: center; justify-content: center; gap: 50px;
  }
  .card {
    position: relative; width: 525px; height: 300px; overflow: hidden;
    box-shadow: 0 6px 18px rgba(0,0,0,0.18);
  }
  /* front */
  .card-front { background: var(--paper); color: var(--ink); }
  .wordmark {
    position: absolute; left: 40px; top: 88px;
    font-size: 46px; letter-spacing: 14px; color: var(--ink);
  }
  .person {
    position: absolute; right: 40px; top: 112px;
    font-size: 16px; color: var(--ink-soft);
  }
  .person .role { font-size: 12px; margin-left: 4px; }
  .rule-main {
    position: absolute; left: 40px; right: 40px; top: 150px;
    height: 1px; background: var(--rule);
  }
  .rule-contact {
    position: absolute; left: 40px; width: 200px; top: 196px;
    height: 1px; background: var(--rule);
  }
  .contact-list {
    position: absolute; left: 40px; top: 204px; list-style: none;
    font-size: 15px; line-height: 19px; color: var(--ink);
  }
  .contact-list li { display: flex; align-items: center; gap: 8px; }
  .contact-list svg { width: 13px; height: 13px; }
  .address {
    position: absolute; right: 28px; top: 176px; text-align: right;
    font-size: 13px; line-height: 16px; color: var(--ink);
  }
  .bottom-bands { position: absolute; left: 0; bottom: 0; width: 525px; height: 48px; }
  .web-front {
    position: absolute; right: 26px; bottom: 14px;
    font-size: 13px; letter-spacing: 2px; color: #fff;
  }
  /* back */
  .card-back { background: var(--dark-card); color: #fff; }
  .card-back .wordmark-back {
    position: absolute; left: 0; right: 0; top: 108px; text-align: center;
    font-size: 52px; letter-spacing: 16px; color: #fff;
  }
  .card-back .web-back {
    position: absolute; left: 0; right: 0; top: 210px; text-align: center;
    font-size: 13px; letter-spacing: 5px; color: #e8e8e8;
  }
</style>
</head>
<body>
<main class="canvas">
  <section class="card card-front" aria-label="Card front">
    <div class="wordmark">tegvu</div>
    <div class="person">Mark Elswood<span class="role">director</span></div>
    <div class="rule-main"></div>
    <div class="rule-contact"></div>
    <ul class="contact-list">
      <li>
        <svg viewBox="0 0 16 16" aria-hidden="true"><path d="M4 1.5l2.5 3-1.5 1.8c.9 1.8 2.4 3.3 4.2 4.2L11 9l3 2.5-1.6 2.6C7 13.6 2.4 9 1.9 3.1z" fill="none" stroke="#333" stroke-width="1.3"/></svg>
        <span>512 555 0140</span>
      </li>
      <li>
        <svg viewBox="0 0 16 16" aria-hidden="true"><rect x="4" y="1.5" width="8" height="5" fill="none" stroke="#333" stroke-width="1.3"/><rect x="1.5" y="6.5" width="13" height="7" rx="1" fill="#333"/></svg>
        <span>512 555 0141</span>
      </li>
      <li>
        <svg viewBox="0 0 16 16" aria-hidden="true"><rect x="1.5" y="3.5" width="13" height="9" fill="none" stroke="#333" stroke-width="1.3"/><path d="M1.5 3.5L8 9l6.5-5.5" fill="none" stroke="#333" stroke-width="1.3"/></svg>
        <span>info@tegvu.com.au</span>
      </li>
    </ul>
    <div class="address">1480 Harlow Park Rd<br>Linden TX 78010</div>
    <svg class="bottom-bands" viewBox="0 0 525 48" aria-hidden="true">
      <rect x="0" y="34" width="525" height="14" fill="var(--band-grey)"/>
      <polygon points="318,48 330,6 525,6 525,48" fill="var(--dark-card)"/>
    </svg>
    <div class="web-front">www.tegvu.com.au</div>
  </section>

  <section class="card card-back" aria-label="Card back">
    <div class="wordmark-back">tegvu</div>
    <div class="web-back">www.tegvu.com.au</div>
  </section>
</main>
</body>
</html>
```